Graphic to hang inside of fitness studio

This graphic will be printed on vinyl and hung inside of a boutique fitness studio for 2019. Graphic should read YEAR OF POSSIBILITIES.

2018 was called Year of Living Well. We would like something on trend for 2019 to hang within the studio as our 2019 Mantra. It is not a logo but for internal use. I've attached our logo here and the website is www.quillenmovehall.com for additional reference. Thank you.

Target Market(s)

25 to 45 women

Industry/Entity Type

Fitness

Colors

Designer to choose colors to be used in the design.

Requirements
Must have
• On trend for 2019. (no people in image)
• Year of Possibilities in trendy font.
• Easy to read.
• Need text only.
• Do not need graphic images.
Nice to have
• Tintavo colours for 2019
• 2019 design trends for background
Should not have
• Male dominate colour or masculine traits.
• Photos of fitness.
• Photos of people.
• Photos of equipment.

```html
<!DOCTYPE html>
<html lang="en">
<head>
<meta charset="utf-8">
<title>Year of Possibilities 2019 – Quillen Move Hall</title>
<link rel="stylesheet" href="https://fonts.googleapis.com/css2?family=Oswald:wght@200;300;600&family=Roboto+Condensed:wght@400;700&display=swap">
<style>
  :root {
    --teal: #2fa59e;
    --teal-light: #3fbcb3;
    --teal-deep: #1f7f7a;
    --navy: #0f2a4a;
    --grey-band: #5b5b5b;
    --grey-band-light: #7a7a7a;
    --grey-dark: #2a2a2a;
    --magenta: #8a2a6e;
    --white: #ffffff;
    --ink: #111418;
  }
  html, body {
    margin: 0;
    padding: 0;
    overflow: hidden;
    background: var(--ink);
  }
  .poster {
    position: relative;
    width: 849px;
    height: 1200px;
    overflow: hidden;
  }
  .poster-art {
    display: block;
    width: 849px;
    height: 1200px;
  }
  .year-number {
    font-family: "Oswald", sans-serif;
    font-weight: 200;
    fill: var(--white);
  }
  .mantra-lead {
    font-family: "Oswald", sans-serif;
    font-weight: 300;
    fill: var(--white);
  }
  .mantra-main {
    font-family: "Oswald", sans-serif;
    font-weight: 600;
    fill: var(--white);
  }
  .studio-name {
    position: absolute;
    top: 104px;
    left: 620px;
    width: 190px;
    margin: 0;
    text-align: center;
    font-family: "Roboto Condensed", sans-serif;
    font-weight: 700;
    font-size: 17px;
    letter-spacing: 0.5px;
    color: var(--teal-light);
    padding-bottom: 8px;
    border-bottom: 1px solid var(--white);
  }
  .studio-web {
    position: absolute;
    top: 144px;
    left: 620px;
    width: 190px;
    margin: 0;
    text-align: center;
    font-family: "Roboto Condensed", sans-serif;
    font-weight: 700;
    font-size: 11px;
    color: var(--white);
  }
</style>
</head>
<body>
<main class="poster">
  <svg class="poster-art" viewBox="0 0 849 1200" xmlns="http://www.w3.org/2000/svg">
    <defs>
      <linearGradient id="lower-photo-tone" x1="0" y1="0" x2="1" y2="0">
        <stop offset="0" stop-color="var(--magenta)"/>
        <stop offset="0.45" stop-color="#1d7f80"/>
        <stop offset="0.8" stop-color="#1a4d6a"/>
        <stop offset="1" stop-color="var(--navy)"/>
      </linearGradient>
      <linearGradient id="lower-photo-shade" x1="0" y1="0" x2="0" y2="1">
        <stop offset="0" stop-color="#000" stop-opacity="0.35"/>
        <stop offset="0.6" stop-color="#000" stop-opacity="0"/>
        <stop offset="1" stop-color="#000" stop-opacity="0.55"/>
      </linearGradient>
      <linearGradient id="upper-photo-tone" x1="0" y1="0" x2="1" y2="1">
        <stop offset="0" stop-color="#6e6e6e"/>
        <stop offset="0.5" stop-color="#3e3e3e"/>
        <stop offset="1" stop-color="#1c1c1c"/>
      </linearGradient>
      <linearGradient id="teal-band-tone" x1="0" y1="0" x2="0" y2="1">
        <stop offset="0" stop-color="var(--teal-light)"/>
        <stop offset="1" stop-color="var(--teal-deep)"/>
      </linearGradient>
      <linearGradient id="grey-band-tone" x1="0" y1="0" x2="0" y2="1">
        <stop offset="0" stop-color="var(--grey-band-light)"/>
        <stop offset="1" stop-color="var(--grey-band)"/>
      </linearGradient>
    </defs>

    <rect class="lower-photo" x="0" y="560" width="849" height="640" fill="url(#lower-photo-tone)" role="img" aria-label="Photo of a woman doing a push-up on a studio floor, tinted magenta to teal"/>
    <rect x="0" y="560" width="849" height="640" fill="url(#lower-photo-shade)"/>

    <g transform="skewY(-17)">
      <rect class="upper-photo" x="0" y="-400" width="849" height="1180" fill="url(#upper-photo-tone)" role="img" aria-label="Black and white photo of a smiling woman doing sit-ups in a gym"/>

      <rect class="band-shadow" x="0" y="845" width="305" height="50" fill="var(--navy)"/>
      <rect class="band-year" x="0" y="690" width="300" height="160" fill="url(#teal-band-tone)"/>

      <rect class="band-shadow" x="295" y="915" width="554" height="25" fill="var(--grey-dark)"/>
      <rect class="band-mantra" x="295" y="750" width="554" height="170" fill="url(#grey-band-tone)"/>

      <text class="year-number" x="78" y="814" font-size="142" textLength="200" lengthAdjust="spacingAndGlyphs">2019</text>
      <text class="mantra-lead" x="320" y="738" font-size="56" textLength="150" lengthAdjust="spacingAndGlyphs">YEAR OF</text>
      <text class="mantra-main" x="328" y="872" font-size="104" textLength="472" lengthAdjust="spacingAndGlyphs">POSSIBILITIES</text>
    </g>
  </svg>

  <p class="studio-name">QUILLEN MOVE HALL</p>
  <p class="studio-web">www.quillenmovehall.com</p>
</main>
</body>
</html>
```